Vertical retractable banner/pop-up for conference

We need a banner for a personal tax business based in Luxembourg to use at conferences/presentations etc.

The company name is Morvane Tax & Consulting - please view the website www.morvanetax.example for the style of our business and use of colours.

The colours we use are:-
#7D1935
#4A96AD
#F5F3EE

Also uploaded are the logo files and the template from the printing company to ensure that the sizes/margins are correct.

Requirements
Must have
• Use of corporate colours (see above).
• Logo
• Website address
Nice to have
• We are open to ideas on style so do not want to prescribe too much as we would like to receive a variety of possible designs ranging from the more minimalist options to more detailed. Some considerations for the design could be to use:-
• 1) The tagline from the website - "Specialists in personal and expatriate taxation".
• 2) The website background is a picture of Luxembourg - if similar city pictures are used on the banner then they should be of Luxembourg also (i.e. not other cities).

```html
<!DOCTYPE html>
<html lang="en">
<head>
<meta charset="UTF-8">
<title>Morvane Tax &amp; Consulting – Conference Banner</title>
<link rel="stylesheet" href="https://fonts.googleapis.com/css2?family=Source+Sans+3:ital,wght@0,400;0,600;0,700;1,400&display=swap">
<style>
  :root {
    --canvas: #f3f4ef;
    --maroon: #6d0a35;
    --maroon-deep: #5a0629;
    --magenta: #b3286e;
    --white: #ffffff;
    --yellow: #f6d21a;
    --button-top: #ffe36a;
    --button-bottom: #f2a900;
    --button-text: #8a1020;
    --arrow-red: #d8261e;
    --photo-sky: #101c4a;
    --photo-mid: #4a3a2a;
    --photo-crowd: #8a1a28;
  }
  * { margin: 0; padding: 0; box-sizing: border-box; }
  html, body { width: 1200px; height: 1000px; overflow: hidden; }
  body {
    background: var(--canvas);
    font-family: "Source Sans 3", sans-serif;
    position: relative;
  }
  .banner {
    position: absolute;
    left: 139px; top: 53px;
    width: 371px; height: 867px;
    overflow: hidden;
    background: var(--maroon);
  }
  .banner-shapes { position: absolute; inset: 0; }
  .brand {
    position: absolute;
    display: flex; align-items: center; gap: 12px;
  }
  .brand-mark { border-radius: 50%; flex: none; }
  .brand-name { font-weight: 600; line-height: 1; }
  .brand-name .line-main { display: block; letter-spacing: 0.5px; }
  .brand-name .line-sub { display: block; letter-spacing: 0.4px; margin-top: 4px; }
  .banner-brand { left: 66px; top: 40px; color: var(--white); }
  .banner-brand .brand-mark { width: 64px; height: 64px; border: 2px solid var(--white); }
  .banner-brand .line-main { font-size: 34px; }
  .banner-brand .line-sub { font-size: 14.5px; }
  .website {
    position: absolute; left: 0; width: 100%; top: 126px;
    text-align: center; color: var(--white);
    font-size: 23px; letter-spacing: 0.3px;
  }
  .pitch {
    position: absolute; left: 0; width: 100%; top: 637px;
    text-align: center; color: var(--white);
    font-weight: 700; text-transform: uppercase;
    font-size: 25px; line-height: 34px;
  }
  .pitch .highlight { color: var(--yellow); display: block; }
  .reassure {
    position: absolute; left: 0; width: 100%; top: 746px;
    text-align: center; color: var(--white);
    font-style: italic; font-size: 22px;
  }
  .cta {
    position: absolute; left: 66px; top: 797px;
    width: 230px; height: 42px; border-radius: 21px;
    background: linear-gradient(var(--button-top), var(--button-bottom));
    box-shadow: 0 2px 3px rgba(0,0,0,0.35);
    display: flex; align-items: center; justify-content: center; gap: 38px;
    color: var(--button-text); font-weight: 700; font-size: 20px;
    padding-left: 16px;
  }
  .cta svg { width: 22px; height: 22px; }
  .corner-brand { left: 865px; top: 828px; color: var(--maroon); }
  .corner-brand .brand-mark { width: 72px; height: 72px; border: 2px solid var(--maroon); }
  .corner-brand .line-main { font-size: 38px; }
  .corner-brand .line-sub { font-size: 15px; }
</style>
</head>
<body>
  <div class="banner">
    <svg class="banner-shapes" viewBox="0 0 371 867" width="371" height="867">
      <defs>
        <linearGradient id="cityPhoto" x1="0" y1="0" x2="0" y2="1">
          <stop offset="0" stop-color="var(--photo-sky)"/>
          <stop offset="0.45" stop-color="var(--photo-mid)"/>
          <stop offset="1" stop-color="var(--photo-crowd)"/>
        </linearGradient>
      </defs>
      <rect class="city-photo" x="0" y="140" width="371" height="530" fill="url(#cityPhoto)" role="img" aria-label="Night view of Luxembourg's old town with an illuminated abbey and a large crowd at an open-air concert"/>
      <path class="top-panel" d="M0 0 H371 V148 Q230 222 0 212 Z" fill="var(--maroon)"/>
      <path class="top-swoosh" d="M0 212 Q230 222 371 148 V160 Q235 236 0 228 Z" fill="var(--magenta)"/>
      <path class="bottom-swoosh" d="M0 588 Q210 590 371 650 V668 Q200 608 0 606 Z" fill="var(--magenta)" opacity="0.85"/>
      <path class="bottom-panel" d="M0 600 Q200 602 371 664 V867 H0 Z" fill="var(--maroon)"/>
    </svg>

    <div class="brand banner-brand">
      <span class="brand-mark"></span>
      <span class="brand-name"><span class="line-main">MORVANE</span><span class="line-sub">TAX &amp; CONSULTING</span></span>
    </div>
    <p class="website">www.morvanetax.example</p>

    <h2 class="pitch">Want<span class="highlight">Correct and efficient</span>Tax compliance ?</h2>
    <p class="reassure">We can help you .</p>
    <a class="cta">Learn more
      <svg viewBox="0 0 22 22"><circle cx="11" cy="11" r="10" fill="var(--arrow-red)"/><path d="M9 6 L14 11 L9 16" fill="none" stroke="#fff" stroke-width="2.4" stroke-linecap="round" stroke-linejoin="round"/></svg>
    </a>
  </div>

  <div class="brand corner-brand">
    <span class="brand-mark"></span>
    <span class="brand-name"><span class="line-main">MORVANE</span><span class="line-sub">TAX &amp; CONSULTING</span></span>
  </div>
</body>
</html>
```